Clausewise - Training I Consulting I Review - Related to Contracts/Agreements

We provide legal services, we need a plattform to book video online trainings or local trainings classes and appointments (with calendar feature to select date and see availability at screen), payment over internet, legal document creation over webpage, videos will be produces in the next 3 - 4 moths so this is a place holder item. Participants for the Online trainings shall have a login in area with secured password. Appointments for local trainings and Consulting. Consider Outline in file attached. I can send you also a video with more explanation regarding the purpose.

Target Market(s)

Startup/scale up Software companies that intent to have an international business and need help with their contracts, to sell their products. Sales persons.

Industry/Entity Type

Legal

Coding

Coded - Design and coding required

Number of Pages Required

5+ page

Font styles to use
Serif
Sans Serif

Colors
000000
eeeeee
f5f5f5
ffffff
f8fcfd
3277b5
ecf7fb
cadf82
86cfc6

Requirements
Must have
• See file clausewise attached with outline. Moreover see here first starting point: https://tomas-vendrell.pagebuildr.example/mysite-1 . Main inspiration comes from www.advisoryhub.example from the log in area, see the outline in the file attached with the screen shots. At the end I need someone who can draft the full webpage and maintain it for a yearly fee. It must be simple and well structured layout. Lean. 1st landing page shall not scroll, 2 landing page only a little to see the testimonials and foster of page. There should be a Progress Bar to indicate the booking/selection process. Calendar booking. Easy fast booking.
• I like the colour mix, the feeling and the easy structor of:
• https://www.artmarket.example/design/6374387or
• https://www.artmarket.example/design/6372391 or https://www.artmarket.example/design/6374366
• https://www.vendorgrid.example/en/web-design/belgium-be
• https://www.artmarket.example/design/5896857
• https://www.artmarket.example/design/5902173
• https://www.artmarket.example/design/17197349
• https://www.artmarket.example/design/5464461
• https://www.artmarket.example/design/7180908
Nice to have
• page for evaluation and interview, see outline attached in the file with screen shots. Document upload.
Should not have
• many pictures, long scroll down pages on the 1st and 2nd ladding pages, many colours and forms. No need for news letter, search field, no need for links to Chatterly and other social media (except workNet).

```html
<!DOCTYPE html>
<html lang="en">
<head>
<meta charset="utf-8">
<title>Clausewise – Contract Training, Design and Consulting</title>
<link href="https://fonts.googleapis.com/css2?family=Poppins:wght@300;400;500&family=Marcellus&display=swap" rel="stylesheet">
<style>
:root{
  --black:#000000;
  --ink:#555555;
  --muted:#8a8a8a;
  --white:#ffffff;
  --band:#f5f9fa;
  --green:#cadf82;
  --teal:#86cfc6;
  --blue:#3ea6d6;
  --gold:#e6b400;
  --footer:#222222;
  --footer-text:#d8d8d8;
  --leaf:#d9e88f;
}
*{margin:0;padding:0;box-sizing:border-box}
html,body{width:750px;height:1200px;overflow:hidden}
body{position:relative;font-family:"Poppins",sans-serif;background:var(--white);color:var(--ink)}
.abs{position:absolute}

/* hero */
.hero{left:0;top:0;width:750px;height:408px;overflow:hidden}
.hero-photo{position:absolute;inset:0;background:radial-gradient(ellipse at 62% 45%,#3a3632 0%,#24211f 45%,#131211 100%)}
.hero-nav{position:absolute;inset:0}
.hero-nav text{font-family:"Marcellus",serif}

/* services */
.services{left:0;top:408px;width:750px;height:306px;background:var(--band)}
.service{top:48px;width:187px;height:206px;text-align:center;box-shadow:0 2px 8px rgba(0,0,0,.08)}
.service--training{left:70px;background:var(--green);color:var(--white)}
.service--design{left:281px;background:var(--white);color:var(--ink)}
.service--consulting{left:492px;background:var(--teal);color:var(--white)}
.service-icon{position:absolute;left:82px;top:20px;width:24px;height:24px}
.service-title{position:absolute;left:0;right:0;top:46px;font-weight:300;font-size:13.5px}
.service-rule{position:absolute;left:83px;top:69px;width:20px;height:1px;background:currentColor}
.service-text{position:absolute;left:12px;right:12px;top:87px;font-size:7.6px;line-height:14px;font-weight:300}
.service-btn{position:absolute;left:66px;top:167px;width:54px;height:18px;line-height:18px;font-size:6.5px;letter-spacing:.3px}
.service--training .service-btn{background:var(--white);color:var(--green)}
.service--design .service-btn{background:#888;color:var(--white)}
.service--consulting .service-btn{background:var(--white);color:var(--teal)}

/* testimonials */
.testimonials-title{left:0;width:750px;top:750px;text-align:center;font-weight:300;font-size:20px;color:#666}
.testimonials-intro{left:150px;width:450px;top:784px;text-align:center;font-size:7.6px;line-height:14px;color:var(--muted);font-weight:300}
.review{width:192px;background:var(--white);box-shadow:0 2px 12px rgba(0,0,0,.1);text-align:center}
.review-stars{position:absolute;left:10px;top:14px}
.review-date{position:absolute;right:12px;top:14px;font-size:8px;color:#666}
.review-quote{position:absolute;left:14px;right:14px;top:47px;font-size:7.6px;line-height:13.5px;color:var(--muted);font-weight:300}
.review-name{position:absolute;left:0;right:0;top:96px;font-size:8px;color:var(--blue)}
.review-avatar{position:absolute;left:75px;top:118px;width:42px;height:42px;border-radius:50%;background:radial-gradient(circle at 50% 40%,#d9c6b6,#9c8a7c)}

/* footer */
.footer{left:0;top:1081px;width:750px;height:119px;background:var(--footer)}
.footer-link{font-size:7.6px;color:var(--footer-text)}
.footer-brand{left:548px;top:37px;font-family:"Marcellus",serif;font-size:15px;color:#8d8d8d}
.footer-rule{left:70px;top:84px;width:610px;height:1px;background:#3a3a3a}
.footer-copy{left:0;width:750px;top:95px;text-align:center;font-size:7.2px;color:#9a9a9a}
</style>
</head>
<body>

<header class="hero abs">
  <div class="hero-photo" role="img" aria-label="Dimmed photo of hands typing on a laptop showing a login screen"></div>
  <svg class="hero-nav" width="750" height="408" viewBox="0 0 750 408">
    <g fill="#0b0b0b" stroke="#2b2b2b" stroke-width="1">
      <polygon points="374,86 428,138 374,190 320,138"/>
      <polygon points="290,172 344,226 290,280 236,226"/>
      <polygon points="458,172 512,226 458,280 404,226"/>
      <polygon points="374,170 426,222 374,274 322,222" fill="#000"/>
    </g>
    <g fill="none" stroke="#bbb" stroke-width="1.2">
      <path d="M368 120l14 14M382 120l-14 14M366 122l4-4M380 132l4 4"/>
      <rect x="281" y="205" width="18" height="11"/><path d="M278 219h24"/>
      <rect x="450" y="204" width="15" height="12"/><path d="M453 216v5M462 216v5"/>
    </g>
    <text x="374" y="156" text-anchor="middle" font-size="12" fill="var(--leaf)">Design</text>
    <text x="290" y="236" text-anchor="middle" font-size="12" fill="var(--leaf)">Consulting</text>
    <text x="458" y="236" text-anchor="middle" font-size="12" fill="var(--leaf)">Training</text>
    <text x="374" y="227" text-anchor="middle" font-size="15" fill="#fff">Clausewise</text>
  </svg>
</header>

<section class="services abs">
  <article class="service service--training abs">
    <svg class="service-icon" viewBox="0 0 24 24" fill="none" stroke="currentColor" stroke-width="1.2"><rect x="3" y="3" width="18" height="12"/><path d="M8 15v6M16 15v6M6 8h8"/></svg>
    <h3 class="service-title">Contract Training</h3><span class="service-rule"></span>
    <p class="service-text">Sed diam nonummy nibh euismod tincidunt ut laoreet dolore magna aliquam erat volutpat wisi enim ad minim veniam quis nostrud exerci tation ullamco suscipit lobortis si ut aliquip ex ea commodo</p>
    <div class="service-btn">SELECT</div>
  </article>
  <article class="service service--design abs">
    <svg class="service-icon" viewBox="0 0 24 24" fill="none" stroke="currentColor" stroke-width="1.2"><path d="M4 4l16 16M20 4L4 20M3 6l3-3M18 21l3-3"/></svg>
    <h3 class="service-title">Contract Design</h3><span class="service-rule"></span>
    <p class="service-text">Sed diam nonummy nibh euismod tincidunt ut laoreet dolore magna aliquam erat volutpat wisi enim ad minim veniam quis nostrud exerci tation ullamco suscipit lobortis si ut aliquip ex ea commodo</p>
    <div class="service-btn">SELECT</div>
  </article>
  <article class="service service--consulting abs">
    <svg class="service-icon" viewBox="0 0 24 24" fill="none" stroke="currentColor" stroke-width="1.2"><rect x="4" y="5" width="16" height="11"/><path d="M2 19h20M8 10h8"/></svg>
    <h3 class="service-title">Contract Consulting</h3><span class="service-rule"></span>
    <p class="service-text">Sed diam nonummy nibh euismod tincidunt ut laoreet dolore magna aliquam erat volutpat wisi enim ad minim veniam quis nostrud exerci tation ullamco suscipit lobortis si ut aliquip ex ea commodo</p>
    <div class="service-btn">SELECT</div>
  </article>
</section>

<h2 class="testimonials-title abs">Testimonials</h2>
<p class="testimonials-intro abs">Lorem ipsum dolor sit amet, consectetuer adipiscing elit, sed diam nonummy nibh euismod tincidunt ut laoreet dolore magna aliquam erat volutpat. Ut wisi enim ad minim veniam, quis nostrud exerci tation ullamcorper suscipit lobortis.</p>

<article class="review abs" style="left:70px;top:845px;height:170px">
  <svg class="review-stars" width="52" height="10" viewBox="0 0 52 10" fill="var(--gold)"><g id="star"><polygon points="5,0 6.2,3.6 10,3.6 7,5.9 8.1,9.5 5,7.3 1.9,9.5 3,5.9 0,3.6 3.8,3.6"/></g><use href="#star" x="10.5"/><use href="#star" x="21"/><use href="#star" x="31.5"/><use href="#star" x="42"/></svg>
  <span class="review-date">26.03.2018</span>
  <p class="review-quote">I'm more likely to just pick up the phone... Instead of using email, I now speak to people. just pick up the phone...</p>
  <p class="review-name">Harold P, Avonmere</p>
  <div class="review-avatar" role="img" aria-label="Portrait of the reviewer"></div>
</article>
<article class="review abs" style="left:278px;top:834px;height:192px">
  <svg class="review-stars" width="52" height="10" viewBox="0 0 52 10" fill="var(--gold)"><use href="#star"/><use href="#star" x="10.5"/><use href="#star" x="21"/><use href="#star" x="31.5"/><use href="#star" x="42"/></svg>
  <span class="review-date">26.03.2018</span>
  <p class="review-quote">I'm more likely to just pick up the phone... Instead of using email, I now speak to people. just pick up the phone...</p>
  <p class="review-name">Harold P, Avonmere</p>
  <div class="review-avatar" role="img" aria-label="Portrait of the reviewer" style="background:radial-gradient(circle at 50% 40%,#efe0c0,#b9a487)"></div>
</article>
<article class="review abs" style="left:487px;top:845px;height:170px">
  <svg class="review-stars" width="52" height="10" viewBox="0 0 52 10" fill="var(--gold)"><use href="#star"/><use href="#star" x="10.5"/><use href="#star" x="21"/><use href="#star" x="31.5"/><use href="#star" x="42"/></svg>
  <span class="review-date">26.03.2018</span>
  <p class="review-quote">I'm more likely to just pick up the phone... Instead of using email, I now speak to people. just pick up the phone...</p>
  <p class="review-name">Harold P, Avonmere</p>
  <div class="review-avatar" role="img" aria-label="Portrait of the reviewer" style="background:radial-gradient(circle at 50% 40%,#e2c8ae,#8a6a52)"></div>
</article>

<footer class="footer abs">
  <span class="footer-link abs" style="left:71px;top:31px">Evaluation</span>
  <span class="footer-link abs" style="left:71px;top:56px">Market Feedback</span>
  <span class="footer-link abs" style="left:202px;top:31px">Students</span>
  <span class="footer-link abs" style="left:202px;top:56px">Templates</span>
  <span class="footer-link abs" style="left:304px;top:31px">Policies</span>
  <span class="footer-link abs" style="left:304px;top:56px">Tools</span>
  <span class="footer-link abs" style="left:395px;top:31px">Team</span>
  <span class="footer-link abs" style="left:395px;top:56px">Contact</span>
  <span class="footer-brand abs">Clausewise</span>
  <span class="footer-rule abs"></span>
  <p class="footer-copy abs">©2018 clausewise.example</p>
</footer>

</body>
</html>
```